Letterhead Design Project

Based on the attached logo we would like have a designed of stationary.
As we are a management consulting company focused on business development dealing with C-level and one level below we new business cards.
We have decided to use HGP (Harbor Growth Partners) as the business name. The legal name will be Harbor Growth Partners ApS but we will brand us under HGP. The tack line is “Shaping Steady Gains” if we need one.
For legal reasons we need to have the legal name on the letters together with the company no. (cvr. nr. 58197024)
We want to signal the following:
- Serious
- Professional
- Creating Result
- Capable of thinking out of the box and creative
- Fast reactions we will be there when needed
What we do not want to be view as is:
- To smart
- We know better
- We can fix it yesterday
Our Value Proposition is two sited:
- Increasing revenue
- Reduced sales cost or increased efficiency
Therefore, companies can call us when they want to grow or they need to be more efficient.
Our business cards should have a two sided print with the logo incl. the tack line on one side and the detailed information on the other site.
We need to have the following information on the letter head:
- Legal company name
- Cvr nr.
- Address incl. country name (Denmark)
- Main number
- Wed address
Symbols are welcome to be used to guide for the above information.
The following information are expected to be in the personal signature of the letter.
- Name
- Title
- Mobile number
- E-mail address
Updates
Some of you has requested our specific details so here they come:
- Address incl. country name (Denmark): Lyngvejen 42, 2970 Nordby, Denmark
- Main number: +45 5871 3302
- Wed address: www.hgprises.example
Mobile no. are +45 xxxx xxxx or +45 4390 1256
Our e-mail looks like this: firstname.seconname@KLMRISES.EXAMPLE or for me: jonas.halvorsen@klmrises.example
We need the design (file) as finish as posible so we just need to add personal details before printing.
Please be aware that we will prefer designs where we can print the full letter incl. design. As we are communicating on e-mails with pdf versions of the letter we also need to have a design which will print on the clients printers.
Target Market(s)
C level and one level below.
Major local and international Companies.
Industry/Entity Type
Management Consulting
Font styles to use
Colors
Designer to choose colors to be used in the design.
Requirements
Must have
- Use of our logo without tack line

```html
<!DOCTYPE html>
<html lang="en">
<head>
<meta charset="utf-8">
<title>HGP Business Card – Front and Back</title>
<link href="https://fonts.googleapis.com/css2?family=Montserrat:wght@700&family=Questrial&display=swap" rel="stylesheet">
<style>
  :root {
    --page-bg: #e9e9ee;
    --card-white: #f7f8fa;
    --brand-blue: #0a5aa8;
    --brand-blue-light: #2a8bd0;
    --brand-blue-deep: #0657a6;
    --ink-dark: #3b4048;
    --ink-mid: #5a6069;
    --band-grey: #5b616b;
    --icon-blue: #2f6fb3;
  }
  * { box-sizing: border-box; margin: 0; padding: 0; }
  html, body {
    width: 1200px;
    height: 934px;
    overflow: hidden;
    background: var(--page-bg);
  }
  .canvas {
    position: relative;
    width: 1200px;
    height: 934px;
  }
  .card {
    position: absolute;
    left: 240px;
    width: 720px;
    height: 412px;
    border-radius: 3px;
    box-shadow: 0 6px 18px rgba(40, 50, 70, 0.14);
    overflow: hidden;
  }

  /* Back side */
  .card-back {
    top: 37px;
    background: linear-gradient(120deg, var(--brand-blue-light) 0%, var(--brand-blue-deep) 100%);
  }
  .card-back .brand-name {
    position: absolute;
    left: 395px;
    top: 70px;
    font-family: "Montserrat", sans-serif;
    font-weight: 700;
    font-size: 84px;
    letter-spacing: 1px;
    color: #ffffff;
    line-height: 1;
  }

  /* Front side */
  .card-front {
    top: 485px;
    background: var(--card-white);
  }
  .holder {
    position: absolute;
    right: 62px;
    top: 58px;
    text-align: right;
  }
  .holder-name {
    font-family: "Montserrat", sans-serif;
    font-weight: 700;
    font-size: 22px;
    letter-spacing: 0.5px;
    color: var(--ink-dark);
    line-height: 1.1;
  }
  .holder-title {
    font-family: "Questrial", sans-serif;
    font-size: 16px;
    color: var(--ink-mid);
    letter-spacing: 0.5px;
  }
  .card-front .brand-name {
    position: absolute;
    left: 62px;
    top: 150px;
    font-family: "Montserrat", sans-serif;
    font-weight: 700;
    font-size: 76px;
    letter-spacing: 1px;
    color: var(--brand-blue);
    line-height: 1;
  }
  .contact-list {
    position: absolute;
    list-style: none;
    font-family: "Questrial", sans-serif;
    font-size: 16px;
    color: var(--ink-mid);
    letter-spacing: 0.3px;
  }
  .contact-list li {
    display: flex;
    align-items: center;
    gap: 10px;
    height: 24px;
  }
  .contact-list svg { width: 16px; height: 16px; flex: none; }
  .contact-online { left: 300px; top: 262px; }
  .contact-phone  { left: 530px; top: 262px; }
  .address {
    position: absolute;
    left: 30px;
    bottom: 44px;
    width: 245px;
    text-align: right;
    font-family: "Questrial", sans-serif;
    font-size: 16px;
    line-height: 1.5;
    color: var(--ink-mid);
    font-style: normal;
  }
  .band-grey {
    position: absolute;
    left: 0;
    bottom: 0;
    width: 290px;
    height: 26px;
    background: var(--band-grey);
  }
  .band-blue {
    position: absolute;
    left: 298px;
    right: 0;
    bottom: 8px;
    height: 22px;
    background: var(--brand-blue);
  }
</style>
</head>
<body>
<main class="canvas">

  <section class="card card-back" aria-label="Business card, back side">
    <div class="brand-name">HGP</div>
  </section>

  <section class="card card-front" aria-label="Business card, front side">
    <div class="holder">
      <div class="holder-name">MADS ERIKSEN</div>
      <div class="holder-title">Manager</div>
    </div>

    <div class="brand-name">HGP</div>

    <ul class="contact-list contact-online">
      <li>
        <svg viewBox="0 0 16 16" aria-hidden="true">
          <circle cx="8" cy="8" r="8" fill="var(--icon-blue)"/>
          <rect x="4" y="5.2" width="8" height="5.6" rx="0.6" fill="none" stroke="#fff" stroke-width="1"/>
          <path d="M4.3 5.6 L8 8.4 L11.7 5.6" fill="none" stroke="#fff" stroke-width="1"/>
        </svg>
        info@hgprises.example
      </li>
      <li>
        <svg viewBox="0 0 16 16" aria-hidden="true">
          <circle cx="8" cy="8" r="7.2" fill="none" stroke="var(--icon-blue)" stroke-width="1.3"/>
          <ellipse cx="8" cy="8" rx="3" ry="7.2" fill="none" stroke="var(--icon-blue)" stroke-width="1"/>
          <path d="M1 8 H15 M2.2 4.6 H13.8 M2.2 11.4 H13.8" stroke="var(--icon-blue)" stroke-width="1"/>
        </svg>
        www.hgprises.example
      </li>
    </ul>

    <ul class="contact-list contact-phone">
      <li>
        <svg viewBox="0 0 16 16" aria-hidden="true">
          <circle cx="8" cy="8" r="7.2" fill="none" stroke="var(--icon-blue)" stroke-width="1.3"/>
          <path d="M5.4 4.2 L6.8 4.2 L7.3 6.2 L6.4 7 C6.9 8.2 7.8 9.1 9 9.6 L9.8 8.7 L11.8 9.2 L11.8 10.6 C11.8 11.3 11.2 11.8 10.5 11.7 C7.6 11.3 4.7 8.4 4.3 5.5 C4.2 4.8 4.7 4.2 5.4 4.2 Z" fill="var(--icon-blue)"/>
        </svg>
        +45 4390 1256
      </li>
      <li>
        <svg viewBox="0 0 16 16" aria-hidden="true">
          <circle cx="8" cy="8" r="8" fill="var(--icon-blue)"/>
          <rect x="5.5" y="3.6" width="5" height="3" fill="#fff"/>
          <rect x="3.6" y="6.4" width="8.8" height="4" rx="0.6" fill="#fff"/>
          <rect x="5.5" y="9.4" width="5" height="3" fill="#fff" stroke="var(--icon-blue)" stroke-width="0.6"/>
        </svg>
        +45 4390 1257
      </li>
    </ul>

    <address class="address">
      Lyngvejen 42, 2970<br>
      Nordby, Denmark
    </address>

    <div class="band-grey"></div>
    <div class="band-blue"></div>
  </section>

</main>
</body>
</html>
```